Website Landing Page for Brightfall Systems

Create a custom designed website landing page for our business. Looking for a professional upscale design that incorporates our logo and logo colors into the theme. I want a standard fixed frame website, not a constant scrolling format that seems to be the trend. To start with I'm looking for more of the graphic design part, maybe a concept or theme, I don't expect to see a finished project. Not interested in generic templates or layouts.

The name of our company is Brightfall Systems and I've attached our logo below. I'd like to have the web page have the same look and feel of our logo, as well as the colors. Our company, Brightfall Systems does system design, installation, and programming, of residential and commercial Audio/Video and Automation systems. We do home theaters, lighting and building automation, video conferencing systems, security camera installations, conference rooms, projectors, distributed audio systems, and similar Technology projects. This will be a professional services/informational website. We will not sell products on this website. This website will be used to advertise our company and communicate our services to prospective customers. Having a well designed, professional and clean website is one way we want to distinguish our company from the competition.

Here are some examples of what I consider a professional well designed website
http://www.qorlamstudio.com/Work/

Last year we had our tradlo store designed (with PixelMarket) and I'm really happy with the way it turned out. You can see it at www.HolvenGearDepot.com I consider this to be a great design and looking for the same level of quality with this new website. However, do not copy or use any part of this design in this new project. This tradlo store is completely separate from our other company Brightfall Systems. I only mention this tradlo store an an example of good work.

Reason: Still going through designs.

Reason: Still working on project and have not had time to review all designs and request revisions.

Reason: Sill going through designs and requesting revisions

Reason: still going through all the submissions we received.

Target Market(s)

People interested in Audio/Video, home theaters, home automation. We do sales, system design, and programming. We typically work on larger projects with both residential and commercial customers.

Industry/Entity Type

Business

Number of Pages Required

1 page

Requirements
Must have
• Great design elements. Please use a white background. I think white goes well with our logo colors.

```html
<!DOCTYPE html>
<html lang="en">
<head>
<meta charset="utf-8">
<title>Brightfall Systems</title>
<link href="https://fonts.googleapis.com/css2?family=Arimo:wght@400;700&display=swap" rel="stylesheet">
<style>
  :root {
    --brand-blue: #3d86d2;
    --nav-blue: #4a8fd6;
    --brand-green: #6cbf45;
    --white: #ffffff;
    --footer-top: #5aa7ea;
    --footer-bottom: #3f7fc4;
  }
  * { margin: 0; padding: 0; box-sizing: border-box; }
  html, body { width: 1200px; height: 1000px; overflow: hidden; background: var(--white); }
  body { font-family: "Arimo", Arial, sans-serif; font-weight: 700; color: var(--brand-blue); }
  .page { position: relative; width: 1200px; height: 1000px; }

  .header-frame { position: absolute; left: 0; top: 0; }
  .brand-name { position: absolute; left: 17px; top: 107px; width: 241px; text-align: center;
    font-size: 17px; line-height: 20px; color: var(--brand-blue); text-transform: uppercase; white-space: nowrap; }

  .main-nav { position: absolute; right: 23px; top: 65px; font-size: 17px; color: var(--nav-blue); white-space: nowrap; }
  .main-nav a { color: var(--nav-blue); text-decoration: none; }

  .intro { position: absolute; left: 28px; top: 196px; width: 290px; text-align: center; }
  .intro-title { font-size: 22px; line-height: 28px; text-transform: uppercase; margin-bottom: 26px; white-space: nowrap; }
  .intro p { font-size: 16px; line-height: 22px; margin-bottom: 15px; white-space: nowrap; }

  .hero-photo { position: absolute; left: 354px; top: 148px; width: 762px; height: 398px;
    background: linear-gradient(180deg, #1d49c9 0%, #3f6fd0 25%, #d9a76a 55%, #c98a4e 80%, #5b4a3a 100%); }

  .sectors { position: absolute; left: 39px; top: 604px; width: 1116px; display: flex; justify-content: space-between; }
  .sector { width: 267px; text-align: center; }
  .sector h2 { font-size: 20px; height: 39px; line-height: 26px; }
  .sector-photo { width: 267px; height: 172px; }
  .photo-auditorium { background: linear-gradient(180deg, #c9c6bf, #5d6a78 60%, #2f3c4c); }
  .photo-building { background: linear-gradient(160deg, #3b79c9, #8fb6e0 50%, #dfe7ee); }
  .photo-conference { background: linear-gradient(180deg, #e8e8e6, #9a6b50 40%, #505356 80%, #2b2b2b); }
  .photo-restaurant { background: linear-gradient(180deg, #3c3a36, #8a7a66 50%, #b5763e 85%, #6c4225); }

  .footer { position: absolute; left: 0; top: 878px; width: 1200px; height: 122px;
    background: linear-gradient(180deg, var(--footer-top), var(--footer-bottom)); }
  .footer::before { content: ""; position: absolute; left: 0; top: 0; width: 100%; height: 8px;
    background: linear-gradient(180deg, #b9e09a, var(--brand-green) 60%, #8fc9e9); }
  .footer-phone { position: absolute; left: 0; top: 48px; width: 100%; text-align: center;
    font-size: 18px; color: #cfe3f7; text-shadow: 0 1px 2px rgba(20, 50, 100, 0.7); }
</style>
</head>
<body>
<div class="page">
  <svg class="header-frame" width="1200" height="150" viewBox="0 0 1200 150" aria-hidden="true">
    <path d="M0 101 H10 V137 H252 V101 H1200" fill="none" stroke="var(--brand-blue)" stroke-width="3"/>
    <path d="M1200 106 H258 V143 H16 V114" fill="none" stroke="var(--brand-green)" stroke-width="3"/>
  </svg>
  <div class="brand-name">Brightfall Systems</div>

  <nav class="main-nav">
    <a href="#">Home</a> | <a href="#">System</a> | <a href="#">Installation</a> | <a href="#">Programming</a> | <a href="#">Audio</a> | <a href="#">Video</a> | <a href="#">Automation</a> | <a href="#">Contact</a>
  </nav>

  <section class="intro">
    <h1 class="intro-title">Brightfall Systems</h1>
    <p>Does system design, installation<br>and programming, of residential<br>and commercial Audio/Video<br>and Automation systems.</p>
    <p>We do home theaters, lighting<br>and building automation,<br>video conferencing systems,<br>security camera installations,<br>conference rooms, projectors,<br>distributed audio systems<br>and similar Technology projects.</p>
  </section>

  <div class="hero-photo" role="img" aria-label="Luxury villa entrance at dusk with palm trees and warm lighting"></div>

  <section class="sectors">
    <div class="sector"><h2>Auditorium.</h2><div class="sector-photo photo-auditorium" role="img" aria-label="Auditorium with tiered seating and projection screen"></div></div>
    <div class="sector"><h2>Building.</h2><div class="sector-photo photo-building" role="img" aria-label="Glass office building under blue sky"></div></div>
    <div class="sector"><h2>Conference.</h2><div class="sector-photo photo-conference" role="img" aria-label="Conference room with long table and wall screen"></div></div>
    <div class="sector"><h2>Resteraunt</h2><div class="sector-photo photo-restaurant" role="img" aria-label="Modern restaurant bar with stools"></div></div>
  </section>

  <footer class="footer">
    <div class="footer-phone">TEL: 5550 1234 87</div>
  </footer>
</div>
</body>
</html>
```